KDR Business Card

Keystone Draper Resources is a successful and reputable financial services company.Our main services are home loans, commercial loans, vehicle finance and equipment finance. We also do development finance for property developers. Our company is always evolving to always be an industry leader in best financial service practices with access to the largest range of lenders in the country.

We want the business card to reflect our national finance company. Modern, professional corporate image. At the same time the concept of Keystone Draper Resources is that we help build wealth for you but the process for the client is an enjoyable peaceful experience. Not stressful at all .....

Colors to be same as the logo .... gold silver black white as the options

On the reverse side of the card I wanted either just the logo symbol or the logo symbol and text of the logo ....

It could be on a black background ..... or silver or gold .... want it to be quite striking to look at when you first see the card.

On the other side of the card I wanted the following details:

Martin Haldane
Director

0438 927 604

martin@kdrgrp.com.au

Po Box 718
Ferndale ACT 2614

www.kdrgrp.com.au

ACN 618 204 957 (This can be in very small print and can be in the bottom corner of the card or somewhere not very prominent)

As requested Ive uploaded the logo file in both .ai and .pdf formats. Please let me know if you need anything else. Thanks

Reason: Still deciding on which design I like best. I will provide individual feedback as well.

```html
<!DOCTYPE html>
<html lang="en">
<head>
<meta charset="utf-8">
<title>Keystone Draper Resources – Business Card</title>
<link rel="stylesheet" href="https://fonts.googleapis.com/css2?family=Cinzel:wght@400;600&family=Orbitron:wght@800&family=Questrial&family=Tinos&display=swap">
<style>
  :root {
    --paper: #ffffff;
    --gold-light: #e7cb96;
    --gold-mid: #dcb46c;
    --gold-deep: #d09c3c;
    --gold-text: #c9a14f;
    --silver: #c4c6c9;
    --silver-edge: #9a9da1;
    --steel: #8e9093;
    --steel-shadow: #cfd0d2;
    --ink-soft: #5c5c5c;
    --on-gold: #ffffff;
  }
  * { margin: 0; padding: 0; box-sizing: border-box; }
  html, body {
    width: 1200px;
    height: 720px;
    overflow: hidden;
    background: var(--paper);
  }
  .card {
    position: relative;
    width: 1200px;
    height: 720px;
    background: var(--paper);
    overflow: hidden;
  }

  /* Brand */
  .brand {
    position: absolute;
    left: 54px;
    top: 60px;
    display: flex;
    align-items: center;
    gap: 22px;
  }
  .brand-disc {
    width: 138px;
    height: 138px;
    border-radius: 50%;
    background: var(--silver);
    border: 4px solid var(--silver-edge);
  }
  .brand-name {
    font-family: "Cinzel", serif;
    font-weight: 600;
    font-size: 34px;
    letter-spacing: 0.02em;
    color: var(--gold-text);
    text-transform: uppercase;
  }

  /* Person */
  .person-name {
    position: absolute;
    left: 92px;
    top: 244px;
    font-family: "Orbitron", sans-serif;
    font-weight: 800;
    font-size: 50px;
    letter-spacing: 0.04em;
    color: var(--steel);
    text-shadow: 4px 4px 0 var(--steel-shadow);
    white-space: nowrap;
  }
  .person-role {
    position: absolute;
    left: 92px;
    top: 316px;
    font-family: "Cinzel", serif;
    font-weight: 400;
    font-size: 42px;
    letter-spacing: 0.98em;
    color: var(--ink-soft);
    text-transform: uppercase;
    white-space: nowrap;
  }

  /* Gold band */
  .gold-band {
    position: absolute;
    left: 0;
    top: 370px;
    width: 1200px;
    height: 350px;
  }

  /* Contact rows */
  .contact {
    position: absolute;
    display: flex;
    align-items: center;
    color: var(--on-gold);
    font-family: "Questrial", sans-serif;
    font-size: 26px;
    line-height: 1.22;
  }
  .contact svg { flex: none; fill: var(--on-gold); }
  .contact-phone   { left: 154px; top: 484px; }
  .contact-email   { left: 154px; top: 580px; }
  .contact-address { left: 692px; top: 474px; }
  .contact-web     { left: 690px; top: 574px; }
  .contact-phone .contact-text,
  .contact-email .contact-text { margin-left: 52px; }
  .contact-address .contact-text { margin-left: 58px; }
  .contact-web .contact-text { margin-left: 52px; }

  .company-number {
    position: absolute;
    right: 46px;
    top: 651px;
    font-family: "Tinos", serif;
    font-size: 16px;
    color: var(--on-gold);
  }
</style>
</head>
<body>
<main class="card">

  <header class="brand">
    <div class="brand-disc"></div>
    <span class="brand-name">Keystone Draper Resources</span>
  </header>

  <h1 class="person-name">MARTIN HALDANE</h1>
  <p class="person-role">Director</p>

  <svg class="gold-band" viewBox="0 0 1200 350" preserveAspectRatio="none" aria-hidden="true">
    <defs>
      <linearGradient id="bandGold" x1="0" y1="0" x2="0" y2="1">
        <stop offset="0" stop-color="#e9cf9d"/>
        <stop offset="0.5" stop-color="#dcb46c"/>
        <stop offset="1" stop-color="#d09c3c"/>
      </linearGradient>
    </defs>
    <polygon points="0,60 978,60 1050,2 1122,60 1200,60 1200,350 0,350" fill="url(#bandGold)"/>
  </svg>

  <div class="contact contact-phone">
    <svg width="56" height="64" viewBox="0 0 56 64" aria-hidden="true">
      <path d="M6 4h8v44H6a4 4 0 0 1-4-4V8a4 4 0 0 1 4-4z"/>
      <rect x="17" y="8" width="36" height="40" rx="4"/>
      <path d="M10 48v8a4 4 0 0 0 4 4h4" stroke="#fff" stroke-width="3" fill="none"/>
      <g fill="#dcb46c">
        <rect x="22" y="13" width="26" height="8"/>
        <rect x="22" y="25" width="6" height="5"/><rect x="32" y="25" width="6" height="5"/><rect x="42" y="25" width="6" height="5"/>
        <rect x="22" y="33" width="6" height="5"/><rect x="32" y="33" width="6" height="5"/><rect x="42" y="33" width="6" height="5"/>
        <rect x="22" y="41" width="6" height="4"/><rect x="32" y="41" width="6" height="4"/><rect x="42" y="41" width="6" height="4"/>
      </g>
    </svg>
    <span class="contact-text">0438 927 604</span>
  </div>

  <div class="contact contact-email">
    <svg width="56" height="40" viewBox="0 0 56 40" aria-hidden="true">
      <rect x="0" y="0" width="56" height="40"/>
      <path d="M2 2l26 20L54 2M2 38l19-18M54 38L35 20" stroke="#dcb46c" stroke-width="2.5" fill="none"/>
    </svg>
    <span class="contact-text">martin@kdrgrp.com.au</span>
  </div>

  <div class="contact contact-address">
    <svg width="44" height="66" viewBox="0 0 44 66" aria-hidden="true">
      <path d="M22 0C10 0 0 10 0 22c0 16 22 44 22 44s22-28 22-44C44 10 34 0 22 0zm0 30a9 9 0 1 1 0-18 9 9 0 0 1 0 18z"/>
    </svg>
    <span class="contact-text">Po Box 718<br>Ferndale ACT 2614</span>
  </div>

  <div class="contact contact-web">
    <svg width="56" height="56" viewBox="0 0 56 56" aria-hidden="true">
      <g fill="none" stroke="#fff" stroke-width="3">
        <circle cx="28" cy="28" r="15"/>
        <ellipse cx="28" cy="28" rx="7" ry="15"/>
        <path d="M13 28h30M16 20h24M16 36h24"/>
        <ellipse cx="28" cy="28" rx="27" ry="9" transform="rotate(-40 28 28)"/>
      </g>
    </svg>
    <span class="contact-text">www.kdrgrp.com.au</span>
  </div>

  <p class="company-number">ACN 618 204 957</p>

</main>
</body>
</html>
```